Kelvo Marine business card

We sell live saltwater fish and live corals
Kelvo Marine
7 Harlow Ct
Sewell, NJ. 08080
(856) 555-0147
Contact Information for Business Card
Kelvo Marine
7 Harlow Ct
Sewell, NJ. 08080
(856) 555-0147
Colors
Designer to choose colors to be used in the design.

```html
<!DOCTYPE html>
<html lang="en">
<head>
<meta charset="utf-8">
<title>Kelvo Marine – Business Card</title>
<link rel="stylesheet" href="https://fonts.googleapis.com/css2?family=Roboto+Condensed:wght@400;700&display=swap">
<style>
  :root {
    --night: #0d0d1c;
    --band: #1b1b36;
    --reef-deep: #1a2350;
    --pink: #e8479a;
    --blue: #1ba6e2;
  }
  html, body {
    margin: 0;
    padding: 0;
    overflow: hidden;
    background: var(--night);
  }
  .card {
    position: relative;
    width: 1200px;
    height: 686px;
    overflow: hidden;
    background: var(--night);
    font-family: "Roboto Condensed", "Arial Narrow", sans-serif;
  }
  .backdrop {
    position: absolute;
    inset: 0;
  }
  .brand {
    position: absolute;
    top: 170px;
    left: 0;
    width: 1200px;
    text-align: center;
  }
  .brand-name {
    margin: 0;
    font-size: 88px;
    font-weight: 700;
    line-height: 1;
    color: var(--pink);
    letter-spacing: 1px;
  }
  .tagline {
    margin: 18px 0 0;
    font-size: 23px;
    font-weight: 700;
    color: var(--pink);
  }
  .address {
    position: absolute;
    top: 365px;
    left: 0;
    width: 1222px;
    text-align: center;
    font-style: normal;
    font-size: 40px;
    line-height: 52px;
    color: var(--pink);
  }
  .phone {
    position: absolute;
    top: 548px;
    left: 0;
    width: 1222px;
    text-align: center;
    font-size: 58px;
    color: var(--blue);
  }
</style>
</head>
<body>
  <div class="card">
    <svg class="backdrop" width="1200" height="686" viewBox="0 0 1200 686">
      <defs>
        <radialGradient id="reefGlow" cx="50%" cy="50%" r="50%">
          <stop offset="0%" stop-color="#24306a" stop-opacity="0.75"/>
          <stop offset="60%" stop-color="#1a2350" stop-opacity="0.45"/>
          <stop offset="100%" stop-color="#0d0d1c" stop-opacity="0"/>
        </radialGradient>
      </defs>
      <polygon class="band band-left" points="194,0 480,0 0,491 0,274" fill="var(--band)"/>
      <polygon class="band band-right" points="731,0 1006,0 1200,217 1200,446" fill="var(--band)"/>
      <ellipse class="reef-photo" role="img" aria-label="Faint photo of a coral colony glowing under blue reef light"
               cx="820" cy="450" rx="250" ry="280" fill="url(#reefGlow)"/>
    </svg>

    <header class="brand">
      <h1 class="brand-name">Nerita Corals LLC</h1>
      <p class="tagline">Suppliers of Quality Corals and Ornamental Saltwater Fish</p>
    </header>

    <address class="address">
      Kelvo Marine<br>
      7 Harlow Ct<br>
      Sewell, NJ. 08080
    </address>

    <div class="phone">(856) 555-0147</div>
  </div>
</body>
</html>
```